A4 Client Referral Program Flyer for Property Management Agency

Harbourline Lettings Group is a property management specialist based on Sydney's Northern Beaches in Australia.

We manage mid to high-end rental properties for investors and property owners.
We are currently looking to build our portfolio and are offering existing clients and contacts a referral incentive. We want to sign up more properties to manage.

We are offering the referrer a $250 referral fee and the new owner 2 months of free management to entice them to use Harbourline Lettings Group.

We want an A4 Flyer to print and add to other document packages we hand out to clients and suppliers.
If at all possible a matching digital banner would be great too! 1000px wide x 250px

Please find copy attached in Word Doc and our logo attached also.

Please see our website for any more details on our business.

We must be able to have an editable photoshop version (PSD) of the document as well as a print ready PDF version incl any bleed necessary for A4 printing.

Target Market(s)

30-60YO Male and Female

Industry/Entity Type

Real Estate

Font styles to use
Sans Serif

Requirements
Must have
• Company Logo, contact details and copy provided

```html
<!DOCTYPE html>
<html lang="en">
<head>
<meta charset="utf-8">
<title>Harbourline Lettings Group – Referral Program Flyer</title>
<link rel="stylesheet" href="https://fonts.googleapis.com/css2?family=Open+Sans:wght@400;600;700;800&display=swap">
<style>
  :root {
    --canvas-bg: #d9dadc;
    --paper: #ffffff;
    --ink: #262626;
    --teal-deep: #1c7883;
    --teal-bright: #2ba7a8;
    --teal-band: #2fa9a9;
    --teal-dark-band: #197582;
    --footer-dark: #242424;
    --sky-top: #c9dde9;
    --sky-bottom: #e9f1f5;
    --foliage: #5e7f4e;
    --facade: #6b7a84;
  }
  * { box-sizing: border-box; margin: 0; padding: 0; }
  html, body {
    width: 1200px; height: 1200px; overflow: hidden;
    background: var(--canvas-bg);
    font-family: "Open Sans", sans-serif;
  }
  .flyer {
    position: absolute; left: 190px; top: 20px;
    width: 820px; height: 1160px;
    background: var(--paper);
    overflow: hidden;
    box-shadow: 0 6px 24px rgba(0,0,0,0.18);
  }
  .brand {
    position: absolute; top: 52px; right: 56px;
    display: flex; align-items: center; gap: 12px;
    font-weight: 700; font-size: 26px; color: var(--ink);
    letter-spacing: 0.5px; text-transform: uppercase;
  }
  .brand-mark {
    width: 18px; height: 18px; background: var(--teal-deep);
  }
  .hero-photo {
    position: absolute; left: 0; top: 120px;
    width: 820px; height: 520px;
    background:
      linear-gradient(180deg, rgba(255,255,255,0) 55%, #ffffff 100%),
      linear-gradient(180deg, var(--sky-top) 0%, var(--sky-bottom) 22%, var(--facade) 32%, #4e5c63 48%, var(--foliage) 68%, #7f9a6a 82%, #cfd8cf 100%);
  }
  .headline {
    position: absolute; left: 0; top: 612px; width: 820px;
    text-align: center; color: var(--ink);
  }
  .headline-intro {
    font-size: 50px; font-weight: 400; line-height: 1.1;
  }
  .headline-reward {
    display: inline-block; margin-top: 14px;
    padding: 4px 36px 10px;
    background: var(--teal-deep); color: #fff;
    font-size: 68px; font-weight: 800; line-height: 1.1;
  }
  .headline-bonus {
    margin-top: 10px;
    font-size: 50px; font-weight: 700; line-height: 1.1;
  }
  .headline-offer {
    font-size: 46px; font-weight: 700; line-height: 1.15;
    color: var(--teal-bright);
  }
  .footer-bands {
    position: absolute; left: 0; bottom: 0; width: 820px; height: 280px;
  }
  .terms {
    position: absolute; left: 60px; top: 920px; width: 700px;
    text-align: center; color: #fff;
    font-size: 15px; line-height: 1.45;
  }
  .referral-url {
    position: absolute; left: 0; top: 1030px; width: 820px;
    text-align: center; color: #fff;
    font-size: 20px; letter-spacing: 0.3px;
  }
  .contact-bar {
    position: absolute; left: 0; top: 1082px; width: 820px; height: 78px;
    display: flex; justify-content: center; align-items: center;
    color: #e6e6e6; font-size: 14px;
  }
  .contact-item { padding: 0 20px; }
  .contact-item + .contact-item { border-left: 1px solid var(--teal-bright); }
</style>
</head>
<body>
  <article class="flyer">
    <div class="brand"><span class="brand-mark"></span>Harbourline Lettings Group</div>

    <div class="hero-photo" role="img" aria-label="Photograph of modern terraced townhouses with balconies and landscaped gardens under a clear sky"></div>

    <section class="headline">
      <p class="headline-intro">Invite your friends and</p>
      <p class="headline-reward">Receive $250</p>
      <p class="headline-bonus">and they get 2 months</p>
      <p class="headline-offer">Free Management! *</p>
    </section>

    <svg class="footer-bands" viewBox="0 0 820 280" width="820" height="280" aria-hidden="true">
      <path d="M0 40 Q410 -10 820 20 L820 280 L0 280 Z" fill="#8fd0cf"/>
      <path d="M0 52 Q410 4 820 34 L820 280 L0 280 Z" fill="var(--teal-band)"/>
      <path d="M0 150 Q410 130 820 140 L820 280 L0 280 Z" fill="var(--teal-dark-band)"/>
      <rect x="0" y="202" width="820" height="78" fill="var(--footer-dark)"/>
    </svg>

    <p class="terms">* $250 referral fee paid when the owner you refer signs their property for Management with Harbourline Lettings Group. Your referral must be submitted prior to signing on our website using the referral form on this page.</p>

    <p class="referral-url">http://www.harbourlinelettings.com.au/referral-program/</p>

    <div class="contact-bar">
      <span class="contact-item">0400 555 018</span>
      <span class="contact-item">referrals@harbourlinelettings.com.au</span>
      <span class="contact-item">www.harbourlinelettings.com.au</span>
    </div>
  </article>
</body>
</html>
```